Almost finish design need new idea for a particular area

Hi guys,
The product is baby wet wipe. I m happy with all area, except the side that locate at the side of the product (which I colored in Yellow)
I feel that consumer can not read the stuff easy (fixed stuffs that I tick in Red, no need to change), so I try to surround it by some kind of cloudy effect, but I still not happy, and would expect some other better ideas.
So the task is simple: to create a background for this side surface that can help people read the stuff inside easy. Personally, I think it should look simple, so it will not overshadow the rest main design. But you could try any ideas if you think it will match the whole design.
I m also attached a photo with 2 example of ideas, in which they totally understand my need, but some how still not match my product taste.
So therefore, I decide to come here, to open a contest.
I hope a designer in here could come up with a nice idea.
Thank you for reading this contest.
Ps: Here is google drive link, in case attached file can not open
https://files.plinkvault.net/shared/boxes/4kqzTmRw8PnYd2LsHcVbXe7uJfG3Qa?view=public

```html
<!DOCTYPE html>
<html lang="vi">
<head>
<meta charset="utf-8">
<title>Nubi Super thick – side panel</title>
<link href="https://fonts.googleapis.com/css2?family=Baloo+2:wght@500;700&display=swap" rel="stylesheet">
<style>
  :root {
    --canvas-bg: #e6e7e8;
    --teal: #4bb5bd;
    --teal-deep: #1e9aa5;
    --teal-pale: #a9dcde;
    --pattern-tone: #bfe5e3;
    --label: #ffffff;
    --label-edge: #d8f0f1;
  }
  * { margin: 0; padding: 0; box-sizing: border-box; }
  html, body { width: 1200px; height: 900px; overflow: hidden; background: var(--canvas-bg); }
  .pack {
    position: absolute;
    left: 130px;
    top: 230px;
    width: 940px;
  }
  .pack__top {
    position: relative;
    height: 200px;
    background: linear-gradient(180deg, var(--pattern-tone), var(--teal-pale));
    border-radius: 18px 18px 0 0;
  }
  .pack__lid {
    position: absolute;
    left: 50%;
    top: 50%;
    width: 220px;
    height: 110px;
    transform: translate(-50%, -50%);
    border-radius: 55px;
    background: var(--teal);
    border: 10px solid var(--teal-deep);
  }
  .pack__side {
    height: 250px;
    background: var(--teal);
    border-radius: 0 0 30px 30px;
    display: flex;
    align-items: center;
    justify-content: space-between;
    padding: 0 50px;
  }
  .side-label {
    height: 176px;
    background: var(--label);
    border-radius: 88px;
    box-shadow: 0 0 0 8px var(--label-edge);
    display: flex;
    flex-direction: column;
    align-items: center;
    justify-content: center;
    text-align: center;
    font-family: "Baloo 2", sans-serif;
    color: var(--teal-deep);
    line-height: 1;
  }
  .side-label--brand { width: 380px; }
  .side-label--info { width: 400px; }
  .brand__name { font-size: 80px; font-weight: 700; }
  .brand__sub { font-size: 34px; font-weight: 700; margin-top: 2px; }
  .info__count { display: flex; align-items: center; gap: 6px; }
  .info__num { font-size: 48px; font-weight: 700; }
  .info__unit { text-align: left; }
  .info__unit-word { display: block; font-size: 22px; font-weight: 700; }
  .info__size { display: block; font-size: 13px; font-weight: 500; }
  .info__type { font-size: 24px; font-weight: 700; margin-top: 4px; }
  .info__claim { font-size: 34px; font-weight: 700; margin-top: 8px; }
</style>
</head>
<body>
  <div class="pack">
    <div class="pack__top" role="img" aria-label="Repeating pattern of small cute animals (elephants, lions, crocodiles) in white and green on pale teal">
      <div class="pack__lid"></div>
    </div>
    <div class="pack__side">
      <div class="side-label side-label--brand">
        <div class="brand__name">Nubi</div>
        <div class="brand__sub">Super thick</div>
      </div>
      <div class="side-label side-label--info">
        <div class="info__count">
          <span class="info__num">60</span>
          <span class="info__unit">
            <span class="info__unit-word">miếng</span>
            <span class="info__size">20 x 15 cm</span>
          </span>
        </div>
        <div class="info__type">Khăn giấy ướt</div>
        <div class="info__claim">Dày hơn, sạch hơn</div>
      </div>
    </div>
  </div>
</body>
</html>
```